Lumo Cellar Traders needs a new business card design

Colour theme: Gold + Red preferred
Front side: Main logo with my details as below;
Back side: Theme of some wine glasses or bottles, maybe different color of log together
Lumo Cellar Traders

Leo Park
박 성민 (this is Korean character) on the English typying board: qkr tjdals
Managing Director

Suite 7/5 Harlow Rd
Bayfield WA 6923
Tel) +61(8) 6027 3518
Mob) +61(412) 305 276

leo.park@lumocellartraders.example
lumocellar@lumocellartraders.example
www.lumocellartraders.example

Target Market(s)

Asian Market

Industry/Entity Type

Business

Contact Information for Business Card

Lumo Cellar Traders

Leo Park
박 성민 (this is Korean character) English typying: qkr tjdals
Managing Director

Suite 7/5 Harlow Rd
Bayfield WA 6923
Tel) +61(8) 6027 3518
Mob) +61(412) 305 276

Font styles to use
Serif
Decorative

Colors
ec1f27
f78f21
f04a50
faa54b
cadf82
abd036

Requirements
Must have
• Company Logo & wine theme
Nice to have
• Very simple & modern
Should not have
• No Red Color on the name of Leo Park or 박 성민
• No traditional looking. young and modern look preferred

```html
<!DOCTYPE html>
<html lang="en">
<head>
<meta charset="utf-8">
<title>Lumo Cellar Traders – Business Card</title>
<link rel="stylesheet" href="https://fonts.googleapis.com/css2?family=Dosis:wght@500&family=Montserrat:wght@400;600&family=Great+Vibes&family=Noto+Sans+KR:wght@400&display=swap">
<style>
  :root {
    --page-bg: #e9e4dc;
    --card-dark: #1c0204;
    --card-mid: #3a0508;
    --card-warm: #5c0a0c;
    --gold: #c9a03a;
    --gold-soft: #b48a33;
    --red-label: #e2462c;
    --text-light: #f4eee6;
    --band-glow: rgba(150, 30, 28, 0.35);
  }
  * { box-sizing: border-box; margin: 0; padding: 0; }
  html, body { width: 1200px; height: 1200px; overflow: hidden; }
  body {
    background: var(--page-bg);
    display: flex;
    flex-direction: column;
    align-items: center;
    justify-content: center;
    gap: 56px;
    font-family: "Montserrat", sans-serif;
  }
  .card {
    position: relative;
    width: 900px;
    height: 514px;
    border-radius: 6px;
    overflow: hidden;
    box-shadow: 0 14px 30px rgba(40, 10, 10, 0.28);
  }
  /* ---------- Front ---------- */
  .card--front {
    background: linear-gradient(115deg, var(--card-dark) 0%, var(--card-mid) 60%, var(--card-warm) 100%);
  }
  .card__glow-band {
    position: absolute;
    left: 0;
    right: 0;
    top: 200px;
    height: 170px;
    background: linear-gradient(180deg, rgba(0,0,0,0) 0%, var(--band-glow) 50%, rgba(0,0,0,0) 100%);
  }
  .brand {
    position: absolute;
    top: 120px;
    left: 0;
    right: 0;
    text-align: center;
  }
  .brand__name {
    font-family: "Dosis", sans-serif;
    font-weight: 500;
    font-size: 54px;
    letter-spacing: 3px;
    text-transform: uppercase;
    color: var(--gold);
    line-height: 1;
  }
  .brand__tagline {
    margin-top: 14px;
    font-size: 17px;
    color: var(--gold-soft);
    letter-spacing: 0.5px;
  }
  .divider {
    position: absolute;
    top: 330px;
    left: 120px;
    right: 120px;
    display: flex;
    align-items: center;
    gap: 18px;
  }
  .divider__line { flex: 1; height: 1px; background: var(--gold-soft); opacity: 0.7; }
  .divider__ornament {
    width: 92px;
    height: 20px;
    border-radius: 10px;
    background: linear-gradient(90deg, #8a5a1e, var(--gold), #8a5a1e);
    opacity: 0.85;
  }
  .address {
    position: absolute;
    top: 372px;
    left: 0;
    right: 0;
    text-align: center;
    font-family: "Great Vibes", cursive;
    font-size: 42px;
    color: var(--gold);
    line-height: 1.2;
    white-space: nowrap;
  }
  /* ---------- Back ---------- */
  .card--back {
    background: linear-gradient(120deg, var(--card-mid) 0%, var(--card-dark) 55%, var(--card-dark) 100%);
  }
  .illustration {
    position: absolute;
    left: 70px;
    top: 70px;
    width: 300px;
    height: 380px;
    border-radius: 40% 40% 20% 20%;
    background:
      radial-gradient(circle at 50% 35%, #e8452f 0%, #b8221e 38%, rgba(184,34,30,0) 62%),
      linear-gradient(180deg, rgba(0,0,0,0) 55%, rgba(201,160,58,0.55) 100%);
  }
  .details {
    position: absolute;
    left: 420px;
    top: 58px;
    right: 50px;
  }
  .details__label {
    font-size: 15px;
    color: var(--gold);
    margin-bottom: 4px;
  }
  .details__label--red { color: var(--red-label); }
  .details__name {
    font-weight: 600;
    font-size: 40px;
    color: var(--text-light);
    letter-spacing: 1px;
    line-height: 1.05;
  }
  .details__role {
    margin-top: 6px;
    font-size: 15px;
    color: var(--gold);
  }
  .details__role .korean { font-family: "Noto Sans KR", sans-serif; }
  .details__rule { height: 1px; background: var(--gold-soft); margin: 16px 0 18px; opacity: 0.8; }
  .details__group { margin-bottom: 14px; }
  .details__value {
    font-size: 16px;
    color: var(--text-light);
    line-height: 1.5;
  }
  .details__value small { font-size: 12px; }
</style>
</head>
<body>

  <section class="card card--front" aria-label="Business card front">
    <div class="card__glow-band" role="img" aria-label="Soft flowing line pattern in deep red"></div>
    <div class="brand">
      <div class="brand__name">Lumo Cellar Traders</div>
      <div class="brand__tagline">Connect &amp; Develop Your Business</div>
    </div>
    <div class="divider">
      <span class="divider__line"></span>
      <span class="divider__ornament" role="img" aria-label="Small gold flourish ornament"></span>
      <span class="divider__line"></span>
    </div>
    <p class="address">Suite 7/5 Harlow Rd Bayfield WA 6923</p>
  </section>

  <section class="card card--back" aria-label="Business card back">
    <div class="illustration" role="img" aria-label="Gold wine glass illustration with a red splash shaped like a globe"></div>
    <div class="details">
      <div class="details__label">Name</div>
      <div class="details__name">LEO PARK</div>
      <div class="details__role"><span class="korean">박 성민</span> - qkr tjdals - Managing Director</div>
      <div class="details__rule"></div>
      <div class="details__group">
        <div class="details__label details__label--red">Tel</div>
        <div class="details__value">+61(8) 6027 3518 <small>(phone)</small></div>
        <div class="details__value">+61(412) 305 276 <small>(Cell)</small></div>
      </div>
      <div class="details__group">
        <div class="details__label">web</div>
        <div class="details__value">www.lumocellartraders.example</div>
      </div>
      <div class="details__group">
        <div class="details__label">Email</div>
        <div class="details__value">lumocellar@lumocellartraders.example</div>
        <div class="details__value">leo.park@lumocellartraders.example</div>
      </div>
      <div class="details__rule"></div>
    </div>
  </section>

</body>
</html>
```